Environmentally friendly pharmaceutical delivery service with an electric vehicle

Conspicuous foiling of electric vehicles for the delivery of pharmaceuticals. Important key points are: pharmaceuticals, regional, environmentally friendly, electric, 100% green electricity, extremely fast delivery.

Important: umbrella brand Lindtal-Apotheken (n important). Branches on the trunk: Brookfield Pharmacy, Elm Pharmacy, Valora Pharmacy, Marisa Pharmacy.

Vehicle e-Tarn from QK, year 2020, model key TX58K4, paintwork black

Target Market(s)

Germany, Baden-Wuerttemberg, City of Karlsruhe

Font styles to use
Sans Serif

Requirements
Must have
• The design has to be really eye-catching and of high quality. One should talk about it in the city and rate it positively.
Nice to have
• People in design who draw the eye to the vehicle

```html
<!DOCTYPE html>
<html lang="en">
<head>
<meta charset="utf-8">
<title>Lindtal Apotheke – Delivery Vehicle Wrap</title>
<link rel="stylesheet" href="https://fonts.googleapis.com/css2?family=Poppins:wght@600;700&family=Oswald:wght@500&display=swap">
<style>
  :root {
    --paint-black: #0b0b0c;
    --brand-blue: #2c5f95;
    --band-blue: #254f80;
    --brand-green: #8cc63f;
    --band-green: #b5d334;
    --text-white: #ffffff;
    --page-bg: #ffffff;
  }
  * { margin: 0; padding: 0; box-sizing: border-box; }
  html, body { width: 1200px; height: 1200px; overflow: hidden; background: var(--page-bg); }
  .canvas { position: relative; width: 1200px; height: 1200px; }

  .wrap-panel {
    position: absolute; left: 60px; top: 360px; width: 1080px; height: 360px;
    background: var(--paint-black); border-radius: 28px; overflow: hidden;
  }
  .wrap-bands { position: absolute; inset: 0; width: 100%; height: 100%; }

  .brand-mark {
    position: absolute; left: 300px; top: 120px; width: 110px; height: 110px;
    border-radius: 50%; background: var(--brand-green);
  }
  .brand-name {
    position: absolute; left: 432px; top: 92px;
    font-family: "Poppins", sans-serif; font-weight: 700; line-height: 1;
  }
  .brand-name .primary {
    display: block; font-size: 66px; letter-spacing: 3px; color: var(--brand-blue);
  }
  .brand-name .secondary {
    display: block; font-size: 24px; letter-spacing: 10px; margin-top: 10px;
    padding-left: 72px; color: var(--brand-green);
  }

  .contact {
    position: absolute; right: 95px; top: 118px;
    font-family: "Poppins", sans-serif; font-weight: 600;
  }
  .contact .phone { display: block; font-size: 24px; color: var(--brand-blue); letter-spacing: 1px; }
  .contact .web { display: block; font-size: 11px; color: var(--brand-green); margin-top: 2px; }

  .key-points {
    position: absolute; left: 402px; top: 306px;
    transform: rotate(-11.45deg); transform-origin: left top;
    font-family: "Oswald", sans-serif; font-weight: 500; font-size: 16px;
    color: var(--text-white); text-transform: uppercase; letter-spacing: 0.4px;
    line-height: 21px; white-space: nowrap;
  }
  .key-points .line { display: block; }
  .key-points .line-second { padding-left: 46px; }
  .key-points .point::before { content: "•"; color: var(--brand-green); margin: 0 5px 0 6px; }
</style>
</head>
<body>
<main class="canvas">
  <section class="wrap-panel" aria-label="Vehicle side wrap">
    <svg class="wrap-bands" viewBox="0 0 1080 360" preserveAspectRatio="none" aria-hidden="true">
      <polygon points="290,360 290,330 1080,170 1080,360" fill="var(--band-blue)"/>
      <polygon points="400,360 1080,222 1080,360" fill="var(--band-green)"/>
    </svg>

    <div class="brand-mark" aria-hidden="true"></div>
    <h1 class="brand-name">
      <span class="primary">LINDTAL</span>
      <span class="secondary">APOTHEKE</span>
    </h1>

    <p class="contact">
      <span class="phone">555.014.2870</span>
      <span class="web">www.lindtalapotheke.com</span>
    </p>

    <div class="key-points">
      <span class="line line-first">
        <span class="point">Pharmaceuticals</span>
        <span class="point">Regional</span>
        <span class="point">Environmentally friendly</span>
        <span class="point">Electric</span>
      </span>
      <span class="line line-second">
        <span class="point">100% green electricity</span>
        <span class="point">Extremely fast delivery</span>
      </span>
    </div>
  </section>
</main>
</body>
</html>
```